Vandrel Group — Business Card Design Brief
Overview
Design a double-sided business card for Vandrel Group that highlights our two service arms: Vandrel Communications (telecommunications) and Vandrel Energy (business energy solutions). The card should feel smart and stand out when handed to clients.

Objectives
Showcase our areas of specialty clearly.
Reflect the overall Vandrel / Vandrel Group brand while acknowledging both arms.
Explore using both logos (Communications + Energy) or one unified logo, depending on the design.

Deliverables
One double-sided business card design (front + back).

Content & Copy
Front (preferred): Logo: Vandrel / Vandrel Group
Descriptor: Business Communications | Business Energy
Back:My contact details and company details
Core products: Business Mobile • Telephony • Internet • Business Energy Solutions

Brand & Visual Direction
We have a group logo currently tailored more toward telecoms, plus a separate Vandrel Energy logo.
Please explore layouts that use both logos or just one, whichever works best.
Color: I wouldn't mind seeing an option using our the Blue/Purple gradient from our website (vandrel-example.co.uk), but also open to non-gradient approaches and other colours..

Overall look: Smart, modern, and distinctive.
Format & Print Specs
Double-sided business card format. (Use a standard size

Must-Haves
Front: Vandrel wording or Vandrel Group wording with atleast 1 logo also on front “Business Communications | Business Energy.”

Back: Contact + company details and core products.
A design that stands out while remaining professional.

Nice-to-Have Options
A gradient version using our site’s Blue/Purple gradient.
A non-gradient version.
A dual-logo treatment versus a single-logo treatment.

Thanks
Dominic

```html
<!DOCTYPE html>
<html lang="en">
<head>
<meta charset="utf-8">
<title>Vandrel Business Card</title>
<link rel="stylesheet" href="https://fonts.googleapis.com/css2?family=Montserrat:wght@400;500;800&display=swap">
<style>
  :root {
    --navy: #27226a;
    --ink: #231f5e;
    --blue: #2f6cc0;
    --cyan: #17a9e1;
    --white: #ffffff;
    --page: #e9eaee;
    --text: #1e1e2a;
  }
  * { box-sizing: border-box; margin: 0; padding: 0; }
  html, body { width: 1200px; height: 875px; overflow: hidden; }
  body {
    background: var(--page);
    font-family: "Montserrat", Arial, sans-serif;
    position: relative;
  }
  .card {
    position: absolute;
    top: 283px;
    width: 540px;
    height: 309px;
    border-radius: 18px;
    overflow: hidden;
    box-shadow: 0 10px 28px rgba(20, 20, 40, 0.18);
  }
  .card-front { left: 40px; background: var(--navy); color: var(--white); }
  .card-back { left: 620px; background: var(--white); color: var(--text); }

  /* Front */
  .front-brand {
    position: absolute;
    left: 0; right: 0; top: 96px;
    display: flex; align-items: center; justify-content: center; gap: 16px;
  }
  .brand-dot {
    width: 46px; height: 46px; border-radius: 50%;
    background: linear-gradient(135deg, var(--blue), var(--cyan));
  }
  .brand-name {
    font-weight: 800; font-size: 58px; letter-spacing: 1px; line-height: 1;
  }
  .front-brand .brand-name { color: var(--white); }
  .front-descriptor {
    position: absolute; left: 0; right: 0; top: 204px;
    text-align: center; font-size: 15px; font-weight: 400; letter-spacing: 0.3px;
  }

  /* Back */
  .back-brand {
    position: absolute; right: 40px; top: 58px;
    display: flex; align-items: center; gap: 10px;
  }
  .back-brand .brand-dot { width: 34px; height: 34px; }
  .back-brand .brand-name { font-size: 40px; color: var(--ink); }
  .rule {
    position: absolute; left: 40px; right: 40px; top: 150px;
    height: 1px; background: linear-gradient(90deg, var(--cyan), var(--blue));
  }
  .person { position: absolute; left: 40px; top: 100px; }
  .person-name { font-weight: 800; font-size: 22px; color: var(--ink); letter-spacing: 0.2px; }
  .person-role { font-size: 13px; color: var(--text); margin-top: 1px; }
  .contacts { position: absolute; left: 40px; top: 162px; list-style: none; }
  .contacts li {
    display: flex; align-items: center; gap: 8px;
    font-size: 12.5px; line-height: 20px;
  }
  .contacts svg { width: 11px; height: 11px; flex: none; }
  .address {
    position: absolute; right: 40px; top: 162px;
    text-align: right; font-size: 12.5px; line-height: 18px;
  }
  .band { position: absolute; left: 0; bottom: 0; width: 540px; height: 70px; }
  .products {
    position: absolute; left: 0; right: 20px; bottom: 12px;
    text-align: right; color: var(--white); font-size: 12.5px; font-weight: 500;
  }
</style>
</head>
<body>

<section class="card card-front" aria-label="Card front">
  <div class="front-brand">
    <span class="brand-dot"></span>
    <span class="brand-name">VANDREL</span>
  </div>
  <p class="front-descriptor">Business Communications | Business Energy</p>
</section>

<section class="card card-back" aria-label="Card back">
  <div class="back-brand">
    <span class="brand-dot"></span>
    <span class="brand-name">VANDREL</span>
  </div>

  <div class="person">
    <p class="person-name">OWEN THACKERAY</p>
    <p class="person-role">Founder/CEO</p>
  </div>

  <div class="rule"></div>

  <ul class="contacts">
    <li>
      <svg viewBox="0 0 12 12"><path d="M2.5 1l2 2-1 1.3a6 6 0 0 0 4.2 4.2L9 7.5l2 2-1.5 1.5C5 11 1 7 1 2.5z" fill="#17a9e1"/></svg>
      +44 0161 000 4821
    </li>
    <li>
      <svg viewBox="0 0 12 12"><rect x="1" y="2.5" width="10" height="7" rx="1" fill="#2f6cc0"/><path d="M1.5 3l4.5 3.5L10.5 3" stroke="#fff" fill="none"/></svg>
      info@vandrel-example.co.uk
    </li>
    <li>
      <svg viewBox="0 0 12 12"><circle cx="6" cy="6" r="5" fill="#2f6cc0"/><path d="M1 6h10M6 1c2 2.5 2 7.5 0 10M6 1c-2 2.5-2 7.5 0 10" stroke="#fff" stroke-width="0.8" fill="none"/></svg>
      www.vandrel-example.co.uk
    </li>
  </ul>

  <p class="address">27 Calder Row<br>Manchester England, M2 7QX</p>

  <svg class="band" viewBox="0 0 540 70" preserveAspectRatio="none" aria-hidden="true">
    <defs>
      <linearGradient id="bandFill" x1="0" x2="1" y1="0" y2="0">
        <stop offset="0" stop-color="#2f6cc0"/>
        <stop offset="1" stop-color="#17a9e1"/>
      </linearGradient>
    </defs>
    <path d="M0 70 V62 C0 45 10 38 30 38 H470 C510 38 530 30 540 14 V70 Z" fill="url(#bandFill)"/>
  </svg>
  <p class="products">Business Mobile • Telephony • Internet • Business Energy Solutions</p>
</section>

</body>
</html>
```